SME Business Bookkeeping Brochure

Fully qualified CPA & registered BAS Agent based in Melbourne Australia trading as Cobalt Ledger Services looking for a brochure design to help grow my online bookkeeping business. I work together with clients to streamline their systems and procedures and provide help and support for growing their business. Specialising in set up and training of accounting packages and ongoing upkeep of accounts and administration needs. Would like to see colours to compliment logo attached should communicate working together and financial safety and growth

Industry/Entity Type

Business Service

Requirements
Must have
• Complimentary to website: http://www.cobaltledgerservices.example.au/

```html
<!DOCTYPE html>
<html lang="en">
<head>
<meta charset="utf-8">
<title>Cobalt Ledger Services – Brochure Pages</title>
<link rel="stylesheet" href="https://fonts.googleapis.com/css2?family=Questrial&family=Comfortaa:wght@700&display=swap">
<style>
:root{
  --teal:#1fd8b7;
  --teal-deep:#13a98b;
  --purple:#6b3fa3;
  --ink:#3b3b3b;
  --paper:#ffffff;
  --paper-shade:#f1f2f3;
  --stage:#e4e4e4;
}
*{margin:0;padding:0;box-sizing:border-box}
html,body{width:1200px;height:1200px;overflow:hidden}
body{background:var(--stage);font-family:"Questrial",sans-serif;color:var(--ink);position:relative}
.page{position:absolute;width:360px;height:507px;background:linear-gradient(180deg,var(--paper) 0%,var(--paper-shade) 100%);overflow:hidden;box-shadow:0 2px 6px rgba(0,0,0,.18)}
.page--welcome{left:207px;top:81px}
.page--cover{left:634px;top:81px}
.page--intro{left:207px;top:633px}
.page--reasons{left:634px;top:633px}
.foot-band{position:absolute;left:0;bottom:0;width:100%;height:17px}
.foot-band--teal{background:var(--teal-deep)}
.foot-band--purple{background:var(--purple)}
.photo{position:absolute}
.torn-edge{position:absolute;left:0;width:360px;height:30px;display:block}
.torn-edge path.line{fill:none;stroke-width:3.5;stroke-linejoin:round;stroke-linecap:round}
.web{position:absolute;left:0;width:100%;text-align:center;font-size:11px;color:var(--purple);letter-spacing:.2px}
.web--teal{color:var(--teal-deep);font-weight:bold}
.call{color:var(--purple);font-size:15px;letter-spacing:.3px}
/* welcome page */
.welcome-top{position:absolute;left:0;top:0;width:100%;height:84px;background:var(--teal)}
.circle{position:absolute;border-radius:50%;border:6px solid var(--purple)}
.welcome-title{position:absolute;left:0;width:100%;text-align:center;color:var(--purple);font-size:46px;letter-spacing:-1px;line-height:1}
.welcome-sub{position:absolute;left:0;width:100%;text-align:center;font-size:15px;color:#333;letter-spacing:-.2px}
.about-box{position:absolute;left:33px;top:284px;width:294px;height:154px;border:2px solid var(--teal);background:#fff;padding:14px 17px 0 19px;font-size:8.6px;line-height:1.3;text-align:justify;color:#444}
.about-box p{margin-bottom:6px}
.about-box .call{position:absolute;left:19px;bottom:12px}
.fold{position:absolute;right:-2px;bottom:-2px;width:40px;height:40px}
/* cover page */
.brand-lockup{position:absolute;left:0;top:74px;width:100%;display:flex;justify-content:center;align-items:center;gap:8px}
.brand-lockup .dot{width:12px;height:12px;border-radius:50%;background:var(--teal-deep)}
.brand-name{color:var(--purple);font-size:19px}
.cover-title{position:absolute;left:0;top:378px;width:100%;text-align:center;font-family:"Comfortaa",sans-serif;font-weight:700;font-size:21px;color:var(--purple)}
.cover-tag{position:absolute;left:0;top:408px;width:100%;text-align:center;font-size:18px;line-height:1.25;color:#222}
/* intro page */
.intro-brand{position:absolute;left:24px;top:58px;display:flex;align-items:center;gap:7px}
.intro-brand .dot{width:11px;height:11px;border-radius:50%;background:#fff}
.intro-brand .brand-name{color:#fff;font-size:14px}
.welcome-card{position:absolute;left:38px;top:222px;width:262px;height:122px;background:var(--teal-deep);border-radius:0 0 8px 8px;color:#fff;text-align:center;padding-top:18px}
.welcome-card .big{font-size:48px;line-height:1;letter-spacing:-1px}
.welcome-card .small{font-size:15px;margin-top:4px}
.questions{position:absolute;left:24px;top:369px;width:320px;font-size:8.6px;line-height:1.3;color:#222}
.intro-call{position:absolute;left:0;top:449px;width:100%;text-align:center}
/* reasons page */
.reasons{position:absolute;left:31px;top:40px;width:302px;font-size:8.2px;line-height:1.5;color:#444;text-align:justify}
.reasons h3{color:var(--purple);font-size:8.6px;font-weight:bold;margin-top:10px}
.reasons h3:first-child{margin-top:0}
.reasons p.closing{margin-top:12px}
</style>
</head>
<body>

<!-- Page: welcome -->
<section class="page page--welcome">
  <div class="welcome-top"></div>
  <svg class="torn-edge" style="top:72px" viewBox="0 0 360 30">
    <path d="M0 16 L10 13 L18 15 L26 10 L34 12 L42 8 L52 11 L60 9 L70 13 L80 10 L90 14 L100 11 L110 15 L122 10 L132 12 L142 7 L154 10 L164 8 L176 12 L186 9 L198 13 L208 10 L220 14 L232 9 L242 11 L254 6 L266 10 L276 8 L288 12 L298 10 L310 14 L320 11 L332 15 L344 12 L352 14 L360 12 L360 30 L0 30 Z" fill="#fff"/>
    <path class="line" d="M0 14 L10 11 L18 13 L26 8 L34 10 L42 6 L52 9 L60 7 L70 11 L80 8 L90 12 L100 9 L110 13 L122 8 L132 10 L142 5 L154 8 L164 6 L176 10 L186 7 L198 11 L208 8 L220 12 L232 7 L242 9 L254 4 L266 8 L276 6 L288 10 L298 8 L310 12 L320 9 L332 13 L344 10 L352 12 L360 10" stroke="var(--purple)"/>
  </svg>
  <div class="circle photo" style="left:39px;top:42px;width:134px;height:134px;background:radial-gradient(circle at 55% 50%,#f2a24a 0%,#3a4d6e 40%,#15243c 100%)" role="img" aria-label="Hand touching a glowing network of connected people icons"></div>
  <div class="circle photo" style="left:196px;top:57px;width:120px;height:120px;background:radial-gradient(circle at 60% 35%,#e8c07a 0%,#5a6f8e 45%,#1d2b44 100%)" role="img" aria-label="Hand reaching over small figures on a digital surface"></div>
  <div class="welcome-title" style="top:207px">WELCOME</div>
  <div class="welcome-sub" style="top:253px">TO COBALT LEDGER SERVICES</div>
  <div class="about-box">
    <p>Cobalt Ledger Services proudly taking your stress away by providing expertly managed Bookkeeping Services.</p>
    <p>Cobalt Ledger Services began in February 2011 as a part time business and has gone from strength to strength ever since. Hannah started the business on her own taking care of simple bookkeeping responsibilities and Registered BAS Agent services for a few small clients while working as a full time Finance Manager for an industry leading IT company.</p>
    <span class="call">Call: +61 0400 318 706</span>
    <svg class="fold" viewBox="0 0 40 40"><path d="M40 0 V40 H0 Z" fill="var(--stage)"/><path d="M40 0 L0 40 Q18 22 40 0Z" fill="var(--teal)"/></svg>
  </div>
  <div class="web" style="top:457px">www.cobaltledgerservices.example.au</div>
  <div class="foot-band foot-band--teal"></div>
</section>

<!-- Page: cover -->
<section class="page page--cover">
  <div class="brand-lockup"><span class="dot"></span><span class="brand-name">Cobalt Ledger Services</span></div>
  <div class="photo" style="left:0;top:140px;width:360px;height:196px;background:linear-gradient(135deg,#3c7fb8 0%,#1d3f7a 50%,#13244e 100%)" role="img" aria-label="Businessman drawing a cloud connected to device and media icons"></div>
  <svg class="torn-edge" style="top:128px" viewBox="0 0 360 30">
    <path d="M0 18 L10 15 L18 17 L26 12 L34 14 L42 10 L52 13 L60 11 L70 15 L80 12 L90 16 L100 13 L110 17 L122 12 L132 14 L142 9 L154 12 L164 10 L176 14 L186 11 L198 15 L208 12 L220 16 L232 11 L242 13 L254 8 L266 12 L276 10 L288 14 L298 12 L310 16 L320 13 L332 17 L344 14 L352 16 L360 14 L360 0 L0 0 Z" fill="#f6f7f8"/>
    <path class="line" d="M0 20 L10 17 L18 19 L26 14 L34 16 L42 12 L52 15 L60 13 L70 17 L80 14 L90 18 L100 15 L110 19 L122 14 L132 16 L142 11 L154 14 L164 12 L176 16 L186 13 L198 17 L208 14 L220 18 L232 13 L242 15 L254 10 L266 14 L276 12 L288 16 L298 14 L310 18 L320 15 L332 19 L344 16 L352 18 L360 16" stroke="var(--teal-deep)"/>
  </svg>
  <svg class="torn-edge" style="top:318px" viewBox="0 0 360 30">
    <path d="M0 12 L12 16 L22 13 L32 17 L44 12 L56 15 L66 11 L78 16 L90 13 L102 18 L114 12 L126 15 L138 10 L150 14 L162 12 L174 17 L186 13 L198 16 L210 11 L222 15 L234 12 L246 17 L258 13 L270 16 L282 11 L294 15 L306 12 L318 17 L330 13 L342 16 L352 12 L360 15 L360 30 L0 30 Z" fill="#f1f2f3"/>
    <path class="line" d="M0 10 L12 14 L22 11 L32 15 L44 10 L56 13 L66 9 L78 14 L90 11 L102 16 L114 10 L126 13 L138 8 L150 12 L162 10 L174 15 L186 11 L198 14 L210 9 L222 13 L234 10 L246 15 L258 11 L270 14 L282 9 L294 13 L306 10 L318 15 L330 11 L342 14 L352 10 L360 13" stroke="var(--teal-deep)"/>
  </svg>
  <div class="cover-title">Cobalt Ledger Services</div>
  <div class="cover-tag">The complete answer to all of your<br>bookkeeping wants and needs</div>
  <div class="web web--teal" style="top:457px">www.cobaltledgerservices.example.au</div>
  <div class="foot-band foot-band--purple"></div>
</section>

<!-- Page: intro -->
<section class="page page--intro">
  <div class="photo" style="left:0;top:0;width:360px;height:226px;background:linear-gradient(120deg,#c9ccd8 0%,#8b93ab 40%,#3a4a6c 75%,#d99a4c 100%)" role="img" aria-label="Hand touching a glowing panel above rows of small figures"></div>
  <div class="intro-brand"><span class="dot"></span><span class="brand-name">Cobalt Ledger Services</span></div>
  <svg class="torn-edge" style="top:202px" viewBox="0 0 360 30">
    <path d="M0 16 L10 13 L18 15 L26 10 L34 12 L42 8 L52 11 L60 9 L70 13 L80 10 L90 14 L100 11 L110 15 L122 10 L132 12 L142 7 L154 10 L164 8 L176 12 L186 9 L198 13 L208 10 L220 14 L232 9 L242 11 L254 6 L266 10 L276 8 L288 12 L298 10 L310 14 L320 11 L332 15 L344 12 L352 14 L360 12 L360 30 L0 30 Z" fill="#fff"/>
    <path class="line" d="M0 14 L10 11 L18 13 L26 8 L34 10 L42 6 L52 9 L60 7 L70 11 L80 8 L90 12 L100 9 L110 13 L122 8 L132 10 L142 5 L154 8 L164 6 L176 10 L186 7 L198 11 L208 8 L220 12 L232 7 L242 9 L254 4 L266 8 L276 6 L288 10 L298 8 L310 12 L320 9 L332 13 L344 10 L352 12 L360 10" stroke="var(--purple)"/>
  </svg>
  <div class="welcome-card">
    <div class="big">WELCOME</div>
    <div class="small">TO COBALT LEDGER SERVICES</div>
  </div>
  <div class="questions">
    Do you find there are never enough hours in your day?<br>
    Does your paperwork keep you up late at night?<br>
    Do you want to stick to your day job and stop going home only to start doing your books?<br>
    Are you finances stressing you out?<br>
    Do you want to know more about how your business is really performing?
  </div>
  <div class="intro-call call">Call: +61 0400 318 706</div>
  <div class="foot-band foot-band--teal"></div>
</section>

<!-- Page: reasons -->
<section class="page page--reasons">
  <div class="reasons">
    <h3>Why Us?</h3>
    <p>Reasons why you should outsource your bookkeeping to Cobalt Ledger Services;</p>
    <h3>Save your valuable time</h3>
    <p>Focus on what you enjoy the most: running your business, and let us take care of the paperwork that is required to keep that business compliant and operational.</p>
    <h3>Save money</h3>
    <p>Reduce excessive accounting fees, and let us help you find cost efficiencies within your business.</p>
    <h3>Know the numbers</h3>
    <p>We can provide you with regular reporting on numerous items so that you can always have the most relevant information at the tip of your fingers to make relevant pro-active plans rather then re-active decisions.</p>
    <h3>Convenience</h3>
    <p>We can come to your office, or work remotely using the latest cloud based software solutions.</p>
    <p class="closing">So contact us today for a free, no obligation, initial consultation so we can discuss what is best for your needs.</p>
  </div>
  <div class="photo" style="left:0;top:342px;width:360px;height:148px;background:radial-gradient(circle at 50% 55%,#6fb6ef 0%,#2a63a8 30%,#8a8f99 65%,#d8d9dc 100%)" role="img" aria-label="Glowing globe of photo tiles surrounded by floating screens"></div>
  <svg class="torn-edge" style="top:330px" viewBox="0 0 360 30">
    <path d="M0 16 L10 13 L18 15 L26 10 L34 12 L42 8 L52 11 L60 9 L70 13 L80 10 L90 14 L100 11 L110 15 L122 10 L132 12 L142 7 L154 10 L164 8 L176 12 L186 9 L198 13 L208 10 L220 14 L232 9 L242 11 L254 6 L266 10 L276 8 L288 12 L298 10 L310 14 L320 11 L332 15 L344 12 L352 14 L360 12 L360 0 L0 0 Z" fill="#f7f7f8"/>
    <path class="line" d="M0 14 L10 11 L18 13 L26 8 L34 10 L42 6 L52 9 L60 7 L70 11 L80 8 L90 12 L100 9 L110 13 L122 8 L132 10 L142 5 L154 8 L164 6 L176 10 L186 7 L198 11 L208 8 L220 12 L232 7 L242 9 L254 4 L266 8 L276 6 L288 10 L298 8 L310 12 L320 9 L332 13 L344 10 L352 12 L360 10" stroke="var(--purple)"/>
  </svg>
  <div class="foot-band foot-band--purple"></div>
</section>

</body>
</html>
```